Veteran Reserved Parking Sign 12x18

Steadfast Homefront Kin Alliance is looking to have a new Veteran Reserved Parking Sign designed. Included in the files are our current logo, the rectangle with the name on it. Also included is our Alt Square version that we will often use. There are several other signs that we kind of like as examples, not not asking for exactly like those, we want you to be creative and show us some new ideas. These are full sized parking signs, 12" wide X 18" height.

Target Market(s)

Veterans and Military Friendly Americans

Industry/Entity Type

Veteran Nonprofit

Font styles to use
Other font styles liked:
• Our logo uses the Franklin Heavy Gothic Font but you are not required to use that font in design.

Requirements
Must have
• Our logo needs to be on there and well as SHKA.ORG
Should not have
• CAN NOT Mention Brave Return Initiative or have black silhouettes similar to their logo. SHKA is NOT the same nonprofit.

```html
<!DOCTYPE html>
<html lang="en">
<head>
<meta charset="utf-8">
<title>Reserved Parking – Veterans Only – SHKA</title>
<link rel="stylesheet" href="https://fonts.googleapis.com/css2?family=Montserrat:wght@800&family=Libre+Franklin:wght@900&display=swap">
<style>
  :root {
    --navy: #06244e;
    --red: #ab1f3a;
    --paper: #f4f5f7;
  }
  html, body {
    margin: 0;
    padding: 0;
    width: 871px;
    height: 1200px;
    overflow: hidden;
    background: var(--paper);
  }
  .parking-sign {
    display: block;
    width: 871px;
    height: 1200px;
  }
  .sign-face { fill: var(--paper); }
  .outer-frame { fill: none; stroke: var(--navy); stroke-width: 35; }
  .inner-frame { fill: none; stroke: var(--red); stroke-width: 17; }
  .frame-gap { fill: var(--paper); }
  .header-banner { fill: var(--navy); }
  .header-text {
    font-family: "Montserrat", "Arial Black", sans-serif;
    font-weight: 800;
    font-size: 150px;
    fill: var(--paper);
    text-anchor: middle;
  }
  .emblem-area { fill: url(#emblemTone); }
  .notice-band { fill: var(--red); }
  .notice-text {
    font-family: "Libre Franklin", "Franklin Gothic Heavy", sans-serif;
    font-weight: 900;
    font-size: 225px;
    fill: var(--paper);
  }
  .org-mark { fill: var(--navy); }
  .org-name {
    font-family: "Libre Franklin", "Franklin Gothic Heavy", sans-serif;
    font-weight: 900;
    font-size: 210px;
    fill: var(--red);
  }
  .org-band, .org-rule { fill: var(--red); }
  .org-fullname {
    font-family: "Libre Franklin", "Franklin Gothic Heavy", sans-serif;
    font-weight: 900;
    font-size: 46px;
    fill: var(--paper);
    text-anchor: middle;
  }
  .org-web {
    font-family: "Montserrat", "Arial Black", sans-serif;
    font-weight: 800;
    font-size: 82px;
    fill: var(--navy);
    text-anchor: middle;
  }
</style>
</head>
<body>
<svg class="parking-sign" viewBox="0 0 1645 2240" preserveAspectRatio="none" xmlns="http://www.w3.org/2000/svg">
  <defs>
    <linearGradient id="emblemTone" x1="0" y1="0" x2="1" y2="0">
      <stop offset="0" stop-color="#ab1f3a" stop-opacity="0.35"/>
      <stop offset="0.5" stop-color="#06244e" stop-opacity="0.45"/>
      <stop offset="1" stop-color="#ab1f3a" stop-opacity="0.35"/>
    </linearGradient>
  </defs>

  <rect class="sign-face" x="0" y="0" width="1645" height="2240"/>

  <!-- frame -->
  <rect class="outer-frame" x="130.5" y="92.5" width="1384" height="2045" rx="112"/>
  <rect class="inner-frame" x="168.5" y="130.5" width="1308" height="1996" rx="74"/>
  <rect class="frame-gap" x="314" y="115" width="1014" height="30"/>

  <!-- header -->
  <polygon class="header-banner" points="328,110 1316,110 1316,464 822,578 328,464"/>
  <text class="header-text" x="822" y="308" textLength="846" lengthAdjust="spacingAndGlyphs">RESERVED</text>
  <text class="header-text" x="822" y="438" textLength="718" lengthAdjust="spacingAndGlyphs">PARKING</text>

  <!-- emblem area -->
  <g role="img" aria-label="Winged star emblem in red and navy">
    <rect class="emblem-area" x="312" y="678" width="1021" height="354" rx="24"/>
  </g>

  <!-- notice -->
  <rect class="notice-band" x="160" y="1134" width="1325" height="456"/>
  <text class="notice-text" x="333" y="1347" textLength="979" lengthAdjust="spacingAndGlyphs">VETERANS</text>
  <text class="notice-text" x="570" y="1533" textLength="521" lengthAdjust="spacingAndGlyphs">ONLY</text>

  <!-- organisation -->
  <rect class="org-mark" x="462" y="1718" width="152" height="152"/>
  <text class="org-name" x="628" y="1870" textLength="672" lengthAdjust="spacingAndGlyphs">SHKA</text>
  <rect class="org-band" x="345" y="1890" width="950" height="48"/>
  <text class="org-fullname" x="820" y="1929" textLength="894" lengthAdjust="spacingAndGlyphs">Steadfast Homefront Kin Alliance</text>
  <rect class="org-rule" x="345" y="1952" width="950" height="14"/>
  <text class="org-web" x="822" y="2063" textLength="472" lengthAdjust="spacingAndGlyphs">SHKA.ORG</text>
</svg>
</body>
</html>
```